Marrowind Booking Engine Marketing Site

Hi,
I’m currently in the process of putting together a web application with the intention of providing small resorts/B&Bs/small hotels the ability to allow their customers to book online.
I’m looking to have a design created for a marketing site, to give potential customers additional information about my booking engine, as well as to help drive sign-ups. A lot of the competition out there appears outdated, so I would like something that is more modern and up to date.
I am looking for just the design (i’m a web developer, but I lack the creative skills for a good marketing site)
For some more background, I will be targeting business owners of smaller resorts and Bed & Breakfasts. These are typically family owned small businesses that may only have a 10 room setup. These businesses will also typically have additional amenities that they will have to rent out or sell to their clients ( ex. Spa, fruit basket, water sport rentals). My software will provide them with the ability to sell their amenities as well.
I’m open to different designs, but my main thing is I want it to look modern, and I want it to have several callouts to sign up for my product.
I am looking to have the homepage created, 1 interior page, and a style guide created (to show form fields, H1’s, etc.).
I had a logo created a couple months ago that will be included with this project brief.
If you need any additional information feel free to reach out to me.

Target Market(s)

This site will be targeted small business owners who are running small resorts, Bed and Breakfasts, or any business that provides rooms for their clients.

Industry/Entity Type

Saas

Number of Pages Required

2 page

Font styles to use
Sans Serif

Colors

Designer to choose colors to be used in the design.

Requirements
Must have
• A modern feel, with several CTA's that will drive to the registration page on the homepage. on the internal page, I mostly just need the page layout, I will reuse that page layout. and a style guide if at all possible (include colors, form fields, H1's, etc.)
Nice to have
• maybe a hero image at the top with buttons over the top? again i'm pretty open to most anything.
Should not have
• I like images, but I don't want the page overrun with images. A good balance.

```html
<!DOCTYPE html>
<html lang="en">
<head>
<meta charset="utf-8">
<title>Marrowind Booking Engine</title>
<link href="https://fonts.googleapis.com/css2?family=Roboto:wght@400;500;700&family=Open+Sans:wght@400;600;700&display=swap" rel="stylesheet">
<style>
:root{
  --navy:#0a3f7c;
  --navy-deep:#062c5e;
  --footer:#0b4784;
  --green:#7cbd1c;
  --ink:#1a1a1a;
  --muted:#6b6b6b;
  --grey-bg:#f2f2f2;
  --white:#ffffff;
}
*{margin:0;padding:0;box-sizing:border-box}
html,body{width:1200px;height:2941px;overflow:hidden}
body{position:relative;background:var(--white);font-family:"Open Sans",Arial,sans-serif;color:var(--ink)}
.abs{position:absolute}
h1,h2,h3,h4{font-family:"Roboto",Arial,sans-serif}

/* header */
.brand{left:98px;top:18px;display:flex;align-items:center;gap:8px}
.brand-dot{width:38px;height:38px;border-radius:50%;background:var(--green)}
.brand-name{font-family:"Roboto",sans-serif;font-weight:500;color:var(--navy);font-size:22px;line-height:22px;text-transform:uppercase}
.brand-name span{display:block;font-size:15px;line-height:18px}
.top-contact{top:20px;font-size:13px;color:#444;display:flex;align-items:center;gap:8px}
.signup{left:1022px;top:17px;width:78px;height:26px;border:1.5px solid var(--green);border-radius:14px;color:var(--navy);font-size:12px;font-weight:700;display:flex;align-items:center;justify-content:center}
.nav{top:59px;left:630px;display:flex;gap:0;font-family:"Roboto",sans-serif;font-weight:700;font-size:13px}
.nav a{position:absolute;white-space:nowrap;color:var(--ink);text-decoration:none}

/* hero */
.hero-bg{left:0;top:98px}
.hero-title{left:98px;top:212px;color:var(--white);font-size:44px;font-weight:700;letter-spacing:.5px}
.hero-text{left:98px;top:286px;width:660px;color:var(--white);font-size:19.5px;font-weight:600;line-height:34px;font-family:"Roboto",sans-serif}
.btn-ghost{left:98px;top:423px;width:169px;height:50px;border:2px solid var(--white);border-radius:26px;color:var(--white);font-family:"Roboto",sans-serif;font-weight:700;font-size:14px;display:flex;align-items:center;justify-content:center}
.dots{left:98px;top:507px;display:flex;gap:5px}
.dots i{width:9px;height:9px;border:1.5px solid var(--white);display:block}
.dots i.on{background:var(--white)}
.phone{left:898px;top:222px;width:200px;height:406px;border-radius:26px;background:var(--white);border:2px solid #cfd4da;box-shadow:0 4px 14px rgba(0,0,0,.25)}
.phone-screen{position:absolute;left:12px;top:70px;width:172px;height:270px;background:linear-gradient(180deg,#3a3a3a 0 13%,#8a6b4e 13% 50%,#f4f4f4 50%)}

/* sections */
.section-title{width:1200px;left:0;text-align:center;font-size:33px;font-weight:500}
.body-copy{font-size:13px;color:var(--muted);line-height:28px;text-align:center}
.btn-outline{height:40px;border:1.5px solid var(--green);border-radius:22px;color:var(--green);font-size:12px;font-weight:700;font-family:"Roboto",sans-serif;display:flex;align-items:center;justify-content:center;letter-spacing:.3px}

.services-bg{left:0;top:1000px;width:1200px;height:490px;background:var(--grey-bg)}
.service{top:1141px;width:260px;text-align:center}
.service-ring{width:130px;height:130px;margin:0 auto;border-radius:50%;border:3px solid var(--navy);padding:6px;background:var(--white)}
.service-ring div{width:100%;height:100%;border-radius:50%;border:3px solid var(--navy);display:flex;align-items:center;justify-content:center}
.service h3{margin-top:20px;font-size:19px;font-weight:500}
.service p{margin-top:4px;font-size:13px;color:var(--muted);line-height:25.5px}
.service .more{margin-top:2px;font-size:12.5px;color:var(--green);font-weight:600}
.flow-arrow{top:1190px}

.work-photo{left:98px;top:1569px;width:453px;height:304px;border:6px solid #eee;background:linear-gradient(135deg,#b5a89a,#6f5e52 45%,#d8d4cf 70%,#9a9590)}
.work-title{left:600px;top:1562px;font-size:33px;font-weight:500}
.work-text{left:600px;top:1621px;width:502px;font-size:13px;color:var(--muted);line-height:26px;text-align:justify}

.divider{left:0;top:1954px;width:1200px;height:3px;background:#dfe9c8}

.audience-title{left:98px;top:2018px;font-size:33px;font-weight:500}
.card{top:2094px;width:314px;height:283px;border:1px solid #ddd;background:var(--white);box-shadow:0 1px 4px rgba(0,0,0,.12);overflow:hidden}
.card-photo{position:absolute;left:4px;top:4px;right:4px;bottom:4px}
.card-photo::after{content:"";position:absolute;left:0;right:0;bottom:0;height:45%;background:rgba(255,255,255,.85)}
.card h4{position:absolute;left:0;right:0;top:210px;text-align:center;font-size:19.5px;font-weight:500;z-index:1}
.chev{top:2222px}

/* footer */
.footer-bg{left:0;top:2440px}
.f-col{top:2622px;color:var(--white)}
.f-col h4{font-size:20px;font-weight:400;letter-spacing:.3px;margin-bottom:26px}
.f-list{list-style:none;font-size:13px;line-height:25.6px}
.f-list li{padding-left:30px;position:relative}
.f-list li::before{content:"";position:absolute;left:2px;top:10px;width:7px;height:7px;border-radius:50%;background:var(--white)}
.f-contact{font-size:13px;line-height:25.6px}
.f-contact div{position:relative;padding-left:40px}
.f-contact svg{position:absolute;left:0;top:6px}
.newsletter p{font-size:13px;line-height:25.6px;width:250px}
.news-field{margin-top:20px;width:234px;height:34px;display:flex;background:var(--white)}
.news-field span{flex:1;color:#444;font-size:11px;padding:9px 12px}
.news-field b{width:44px;background:var(--green);display:flex;align-items:center;justify-content:center}
.f-rule{left:0;top:2871px;width:1200px;height:1px;background:rgba(255,255,255,.45)}
.copyright{left:98px;top:2895px;color:var(--white);font-size:13px}
.connect{left:940px;top:2895px;color:var(--white);font-size:13px;display:flex;gap:10px;align-items:center}
.connect i{width:13px;height:13px;border-radius:50%;background:var(--white);display:block}
</style>
</head>
<body>

<!-- header -->
<div class="abs brand"><div class="brand-dot"></div><div class="brand-name">Marrowind<span>Booking Engine</span></div></div>
<div class="abs top-contact" style="left:714px">
  <svg width="12" height="12" viewBox="0 0 24 24"><path fill="#7cbd1c" d="M6.6 10.8a15 15 0 0 0 6.6 6.6l2.2-2.2a1 1 0 0 1 1-.25 11 11 0 0 0 3.6.6 1 1 0 0 1 1 1V20a1 1 0 0 1-1 1A17 17 0 0 1 3 4a1 1 0 0 1 1-1h3.5a1 1 0 0 1 1 1c0 1.2.2 2.4.6 3.6a1 1 0 0 1-.25 1z"/></svg>
  +1 555 010 2040
</div>
<div class="abs top-contact" style="left:850px">
  <svg width="13" height="10" viewBox="0 0 26 20"><rect width="26" height="20" rx="2" fill="#7cbd1c"/><path d="M1 2l12 9 12-9" stroke="#fff" stroke-width="2" fill="none"/></svg>
  info@marrowind.com
</div>
<div class="abs signup">SIGN UP</div>
<nav class="abs nav" style="left:0;width:1200px">
  <a style="left:630px">HOME</a>
  <a style="left:700px">ABOUT US</a>
  <a style="left:801px">SERVICES</a>
  <a style="left:897px">BLOG</a>
  <a style="left:962px">CONTACT US</a>
  <svg class="abs" style="left:1084px;top:2px" width="14" height="14" viewBox="0 0 24 24"><circle cx="10" cy="10" r="7" stroke="#111" stroke-width="3.5" fill="none"/><path d="M15 15l7 7" stroke="#111" stroke-width="4"/></svg>
</nav>

<!-- hero -->
<svg class="abs hero-bg" width="1200" height="580" viewBox="0 0 1200 580">
  <defs>
    <linearGradient id="heroFill" x1="0" y1="0" x2="0" y2="1">
      <stop offset="0" stop-color="#0b3170"/>
      <stop offset="1" stop-color="#0a4287"/>
    </linearGradient>
  </defs>
  <polygon points="0,0 1200,0 1200,446 0,567" fill="url(#heroFill)"/>
  <polygon points="0,534 1200,446 1200,462 0,548" fill="var(--green)"/>
</svg>
<h1 class="abs hero-title">MARROWIND BOOKING ENGINE</h1>
<p class="abs hero-text">We are in the process of putting together a web application with the intention of providing small resorts/B&amp;Bs/small hotels the ability to allow their customers to book online</p>
<div class="abs btn-ghost">BUY NOW !</div>
<div class="abs dots"><i class="on"></i><i></i><i></i><i></i></div>
<div class="abs phone" role="img" aria-label="Smartphone showing a hotel listing and a booking confirmed screen">
  <div class="phone-screen"></div>
</div>

<!-- welcome -->
<h2 class="abs section-title" style="top:697px">Welcome To Marrowind Booking Engine</h2>
<p class="abs body-copy" style="left:160px;top:763px;width:880px">Lorem ipsum dolor sit amet, consectetur adipiscing elit, sed do eiusmod tempor incididunt ut labore et dolore magna aliqua. Ut enim ad minim veniam, quis nostrud exercitation ullamco laboris nisi ut aliquip ex ea commodo consequat. Duis aute irure dolor in reprehenderit in voluptate velit esse cillum dolore eu fugiat nulla pariatur.</p>
<div class="abs btn-outline" style="left:538px;top:879px;width:125px">READ MORE</div>

<!-- services -->
<div class="abs services-bg"></div>
<h2 class="abs section-title" style="top:1066px">Our Services</h2>

<div class="abs service" style="left:76px">
  <div class="service-ring"><div>
    <svg width="44" height="44" viewBox="0 0 24 24" fill="none" stroke="#7cbd1c" stroke-width="1.4"><circle cx="12" cy="12" r="3"/><path d="M12 2v3M12 19v3M2 12h3M19 12h3M4.9 4.9l2.1 2.1M17 17l2.1 2.1M4.9 19.1L7 17M17 7l2.1-2.1"/><circle cx="12" cy="12" r="6.5"/></svg>
  </div></div>
  <h3>IT Strategy</h3>
  <p>Lorem ipsum dolor sit amet,<br>consectetur adipiscing elit, sed do<br>eiusmod tempor incididunt</p>
  <div class="more">Read More ⟶</div>
</div>
<div class="abs service" style="left:337px">
  <div class="service-ring"><div>
    <svg width="50" height="44" viewBox="0 0 28 24" fill="none" stroke="#7cbd1c" stroke-width="1.5"><path d="M2 2v20h24"/><path d="M5 18l6-7 4 4 8-9"/><path d="M19 6h4v4"/></svg>
  </div></div>
  <h3>Development</h3>
  <p>Lorem ipsum dolor sit amet,<br>consectetur adipiscing elit, sed do<br>eiusmod tempor incididunt</p>
  <div class="more">Read More ⟶</div>
</div>
<div class="abs service" style="left:599px">
  <div class="service-ring"><div>
    <svg width="46" height="46" viewBox="0 0 24 24" fill="none" stroke="#7cbd1c" stroke-width="1.4"><rect x="2" y="10" width="5" height="11"/><path d="M7 11l4-8c2 0 2.5 1.5 2 4l-.5 2H20a2 2 0 0 1 1.9 2.4l-1.6 7A2 2 0 0 1 18.4 20H7"/></svg>
  </div></div>
  <h3>Quality</h3>
  <p>Lorem ipsum dolor sit amet,<br>consectetur adipiscing elit, sed do<br>eiusmod tempor incididunt</p>
  <div class="more">Read More ⟶</div>
</div>
<div class="abs service" style="left:860px">
  <div class="service-ring"><div>
    <svg width="40" height="46" viewBox="0 0 20 24" fill="none" stroke="#7cbd1c" stroke-width="1.8"><path d="M10 1v22"/><path d="M16 6c-1-2-3-2.5-6-2.5S4 5 4 7.5 7 10.5 10 11.5s6 2 6 5-3 4-6 4-5-1-6-3"/></svg>
  </div></div>
  <h3>Pricing</h3>
  <p>Lorem ipsum dolor sit amet,<br>consectetur adipiscing elit, sed do<br>eiusmod tempor incididunt</p>
  <div class="more">Read More ⟶</div>
</div>

<svg class="abs flow-arrow" style="left:318px" width="40" height="30" viewBox="0 0 40 30"><path d="M4 8 C 16 2, 28 6, 30 20" stroke="#7cbd1c" stroke-width="6" fill="none"/><path d="M22 18 L31 28 L38 15 Z" fill="#7cbd1c"/></svg>
<svg class="abs flow-arrow" style="left:575px" width="40" height="30" viewBox="0 0 40 30"><path d="M4 12 C 12 24, 26 24, 30 12" stroke="#7cbd1c" stroke-width="6" fill="none"/><path d="M22 12 L33 4 L37 18 Z" fill="#7cbd1c"/></svg>
<svg class="abs flow-arrow" style="left:836px" width="40" height="30" viewBox="0 0 40 30"><path d="M4 8 C 16 2, 28 6, 30 20" stroke="#7cbd1c" stroke-width="6" fill="none"/><path d="M22 18 L31 28 L38 15 Z" fill="#7cbd1c"/></svg>

<!-- what we do -->
<div class="abs work-photo" role="img" aria-label="Person typing on a laptop showing a booking page, desk with calculator and notebook"></div>
<h2 class="abs work-title">What We Do</h2>
<p class="abs work-text">We will be targeting business owners of smaller resorts and Bed &amp; Breakfasts. These are typically family owned small businesses that may only have a 10 room setup. These businesses will also typically have additional amenities that they will have to rent out or sell to their clients ( ex. Spa, fruit basket, water sport rentals). My software will provide them with the ability to sell their amenities as well</p>
<div class="abs btn-outline" style="left:600px;top:1833px;width:124px">READ MORE</div>

<div class="abs divider"></div>

<!-- target audience -->
<h2 class="abs audience-title">Target Audience</h2>
<svg class="abs chev" style="left:42px" width="14" height="20" viewBox="0 0 14 20"><path d="M11 2L3 10l8 8" stroke="#222" stroke-width="3" fill="none"/></svg>
<svg class="abs chev" style="left:1140px" width="14" height="20" viewBox="0 0 14 20"><path d="M3 2l8 8-8 8" stroke="#222" stroke-width="3" fill="none"/></svg>
<div class="abs card" style="left:98px">
  <div class="card-photo" role="img" aria-label="Small beach resort with palm trees and colourful building" style="background:linear-gradient(180deg,#9fd0ea 0%,#5b8f3e 40%,#d9b64a 62%,#3f88c5 100%)"></div>
  <h4>Small Resorts</h4>
</div>
<div class="abs card" style="left:441px">
  <div class="card-photo" role="img" aria-label="Business team meeting around a table in a bright office" style="background:linear-gradient(180deg,#e9e7e4 0%,#cfcac4 45%,#3b3e44 75%,#d8d4cf 100%)"></div>
  <h4>Business To Business</h4>
</div>
<div class="abs card" style="left:784px">
  <div class="card-photo" role="img" aria-label="Small hotel room with red kitchen cabinets and warm lighting" style="background:linear-gradient(90deg,#b83027 0%,#d94a3a 35%,#e6d5b8 60%,#c9ae7e 100%)"></div>
  <h4>Small Hotels</h4>
</div>

<!-- footer -->
<svg class="abs footer-bg" width="1200" height="501" viewBox="0 0 1200 501">
  <polygon points="0,118 1200,8 1200,30 0,132" fill="var(--green)"/>
  <polygon points="0,132 1200,28 1200,501 0,501" fill="var(--footer)"/>
</svg>

<div class="abs f-col" style="left:98px">
  <h4>LINKS</h4>
  <ul class="f-list"><li>Home</li><li>About us</li><li>Services</li><li>Blog</li><li>Contact us</li></ul>
</div>
<div class="abs f-col" style="left:300px">
  <h4>OTHER LINKS</h4>
  <ul class="f-list"><li>Privacy Policy</li><li>Terms &amp; conditions</li><li>FAQ</li><li>Legal</li><li>Sitemap</li></ul>
</div>
<div class="abs f-col" style="left:555px">
  <h4>CONTACT US</h4>
  <div class="f-contact">
    <div><svg width="10" height="14" viewBox="0 0 10 14"><path d="M5 0a5 5 0 0 1 5 5c0 3.5-5 9-5 9S0 8.5 0 5a5 5 0 0 1 5-5z" fill="#fff"/><circle cx="5" cy="5" r="1.8" fill="#0b4784"/></svg>48 Larkfield Row<br>Suite 12-204<br>Westbrook, NH 03271</div>
    <div><svg width="14" height="10" viewBox="0 0 26 20"><rect width="26" height="20" rx="2" fill="#fff"/><path d="M1 2l12 9 12-9" stroke="#0b4784" stroke-width="2" fill="none"/></svg>info@marrowind.com</div>
    <div><svg width="12" height="12" viewBox="0 0 24 24"><path fill="#fff" d="M6.6 10.8a15 15 0 0 0 6.6 6.6l2.2-2.2a1 1 0 0 1 1-.25 11 11 0 0 0 3.6.6 1 1 0 0 1 1 1V20a1 1 0 0 1-1 1A17 17 0 0 1 3 4a1 1 0 0 1 1-1h3.5a1 1 0 0 1 1 1c0 1.2.2 2.4.6 3.6a1 1 0 0 1-.25 1z"/></svg>+1 555 010 2040</div>
  </div>
</div>
<div class="abs f-col newsletter" style="left:865px">
  <h4>NEWSLETTER</h4>
  <p>Subscribe our newsletter for more information</p>
  <div class="news-field"><span>Enter your mail here</span><b><svg width="12" height="12" viewBox="0 0 12 12"><path d="M1 6h9M6 2l4 4-4 4" stroke="#fff" stroke-width="2" fill="none"/></svg></b></div>
</div>

<div class="abs f-rule"></div>
<div class="abs copyright">©2018 Copyrights Marrowind Booking Engine, All Rights Reserved</div>
<div class="abs connect">Connect With Us : <i></i><i></i></div>

</body>
</html>
```